Re jig a A4 Instructional Flyer

We need an established A4 instructional Flyer (2 pages x A4) - to be rejigged in Harcourt College of Learning Branding to look fresh and new.

Permissions have been received to rejig this Medical Triage Chart. Fresh branding and setting out (fonts) required.

FOOTER NOTES : to be inserted at the bottom of the A4 instruction sheet

Harcourt College produced with permissions from Outback Care Alliance, produced by Outback Care Alliance with Clinic Circle Uptown with permissions from Southern Lakes Carewell Hub. Harcourt acknowledges the NBFPS Standards Criterion 3.2.3 Practice Training and Education in Triage

Target Market(s)

Medical Practices

Industry/Entity Type

Health

Font styles to use
Serif

Colors
0255a3
f78f20

Requirements
Must have
• Professional
• Pops of colour in the chart.
• This chart is to be USED and is VISUAL (no boring grey words throughout)
• PROBS SANS SERIF but SERIF for titles OK
Nice to have
• look at www.harcourtlearn.edu.au FOR BRANDING look and feel

```html
<!DOCTYPE html>
<html lang="en">
<head>
<meta charset="utf-8">
<title>Triage: A Guide to Urgency – Harcourt College of Learning</title>
<link rel="stylesheet" href="https://fonts.googleapis.com/css2?family=Cinzel:wght@600;700&family=Cormorant+SC:wght@500&family=Raleway:wght@400;600;700&display=swap">
<style>
  :root {
    --navy: #2e3a5c;
    --panel: #3d4a63;
    --accent: #e9a25e;
    --accent-strong: #f39a3c;
    --ink: #2b2b2b;
    --rule: #5a5a5a;
    --cat1: #f04a3a;
    --cat2: #f26a34;
    --cat3: #f4cf2e;
    --cat4: #1fa98b;
    --cat5: #5b4ea2;
    --cat6: #2fa64c;
    --paper: #ffffff;
  }
  * { box-sizing: border-box; margin: 0; padding: 0; }
  html, body { width: 1200px; height: 848px; overflow: hidden; background: var(--paper); }
  .sheet {
    position: relative; width: 1400px; height: 990px;
    transform: scale(0.857143); transform-origin: 0 0;
    font-family: "Raleway", Arial, sans-serif; color: var(--ink);
  }
  .brand {
    position: absolute; left: 24px; top: 28px; width: 130px;
    text-align: center; color: var(--navy);
    font-family: "Cinzel", Georgia, serif; font-weight: 600; font-size: 11px; line-height: 1.2;
  }
  .brand-mark {
    display: block; width: 48px; height: 48px; margin: 8px auto 0;
    background: var(--navy);
  }
  .title {
    position: absolute; left: 181px; top: 60px;
    font-family: "Cinzel", Georgia, serif; font-weight: 700; font-size: 23px;
    line-height: 28px; color: var(--navy); letter-spacing: 0.3px;
  }
  .rule { position: absolute; left: 181px; right: 12px; height: 2px; background: var(--accent); }
  .rule.top { top: 122px; }
  .rule.bottom { top: 899px; }
  .flow-lines { position: absolute; left: 0; top: 0; }
  .box {
    position: absolute; border: 2px solid var(--navy); background: var(--paper);
    font-size: 13.5px; color: var(--ink); display: flex; align-items: center; justify-content: center;
  }
  .box.question { left: 352px; top: 146px; width: 300px; height: 33px; }
  .box.choice { text-transform: uppercase; letter-spacing: 0.4px; }
  .box.yes { left: 243px; top: 348px; width: 85px; height: 33px; }
  .box.not-now { left: 677px; top: 191px; width: 186px; height: 32px; }
  .box.no { left: 733px; top: 348px; width: 85px; height: 33px; }
  .box.offer { left: 677px; top: 257px; width: 186px; height: 65px; justify-content: flex-start; padding: 0 26px; line-height: 1.25; }
  .box.record {
    left: 352px; top: 237px; width: 301px; height: 181px;
    display: block; padding: 6px 14px 0 36px; line-height: 17px;
  }
  .record p.lead { margin-left: 0; }
  .record p.step::before { content: "\25B6"; color: var(--accent-strong); font-size: 9px; margin-right: 4px; vertical-align: 1px; }
  .emergency {
    position: absolute; left: 895px; top: 146px; width: 262px; height: 272px;
    background: var(--panel); color: #f1f3f7; padding: 14px 10px 0 20px;
    font-size: 13.5px; line-height: 17px;
  }
  .emergency h2 { font-size: 13.5px; font-weight: 700; color: var(--accent-strong); letter-spacing: 0.4px; margin-bottom: 16px; }
  .emergency p { margin-bottom: 16px; }
  .emergency .call { text-align: center; color: var(--accent-strong); font-weight: 700; letter-spacing: 0.3px; margin-left: -10px; }
  .triage-table {
    position: absolute; left: 18px; top: 448px; border-collapse: collapse; table-layout: fixed; width: 1371px;
    font-size: 13.5px; line-height: 17px;
  }
  .triage-table th {
    font-size: 18px; font-weight: 700; height: 35px; text-align: center; vertical-align: top; padding-top: 3px;
  }
  .triage-table th.instruction { color: #111; text-align: left; padding-left: 24px; }
  .triage-table td { border: 1.5px solid var(--rule); vertical-align: top; padding: 4px 5px; }
  .triage-table .symptoms td { height: 204px; }
  .triage-table .action td { height: 61px; padding-top: 6px; }
  .triage-table .staff td { height: 50px; padding-top: 8px; }
  .triage-table .admin td { height: 50px; padding-top: 8px; }
  .triage-table strong { font-weight: 700; }
  .c1 { color: var(--cat1); } .c2 { color: var(--cat2); } .c3 { color: var(--cat3); }
  .c4 { color: var(--cat4); } .c5 { color: var(--cat5); } .c6 { color: var(--cat6); }
  .credits {
    position: absolute; left: 181px; top: 911px; width: 1060px;
    font-family: "Cormorant SC", Georgia, serif; font-weight: 500; font-size: 15px; line-height: 16px;
    color: var(--navy); letter-spacing: 0.2px;
  }
</style>
</head>
<body>
<main class="sheet">
  <div class="brand">Harcourt College<br>of Learning<span class="brand-mark"></span></div>

  <h1 class="title">Triage: A guide to urgency for non-clinical staff in general practice for<br>telephone and walk in presentations</h1>
  <div class="rule top"></div>

  <svg class="flow-lines" width="1400" height="440" viewBox="0 0 1400 440" aria-hidden="true">
    <defs>
      <marker id="arrowhead" markerWidth="8" markerHeight="8" refX="6" refY="4" orient="auto">
        <path d="M0,0 L8,4 L0,8 Z" fill="#e9a25e"/>
      </marker>
    </defs>
    <g fill="none" stroke="#e9a25e" stroke-width="2">
      <path d="M352 162 H285 V344" marker-end="url(#arrowhead)"/>
      <path d="M328 364 H348" marker-end="url(#arrowhead)"/>
      <path d="M652 162 H774 V187" marker-end="url(#arrowhead)"/>
      <path d="M774 223 V253" marker-end="url(#arrowhead)"/>
      <path d="M774 322 V344" marker-end="url(#arrowhead)"/>
      <path d="M733 364 H657" marker-end="url(#arrowhead)"/>
    </g>
  </svg>

  <div class="box question">Do you have an urgent problem?</div>
  <div class="box choice yes">Yes</div>
  <div class="box choice not-now">No / I don't now</div>
  <div class="box offer">The next available<br>appointment is …<br>Is this ok?</div>
  <div class="box choice no">No</div>
  <div class="box record">
    <p class="lead">Record the patient's phone number</p>
    <p class="step">What is the name and age of the patient?</p>
    <p class="step">What is the nature of the problem?</p>
    <p class="step">What is the duration of the problem?</p>
    <p class="step">What is the severity of the problem?</p>
    <p class="step">Has the patient had any previous major health problems?</p>
    <p class="step">Select a category below and follow instructions.</p>
  </div>

  <aside class="emergency">
    <h2>EMERGENCY ACTION PLAN</h2>
    <p>Remain calm and do notpanic</p>
    <p>Be aware and respond to the needs of the emergency</p>
    <p>Assess which patient needs to take priority</p>
    <p>Deal with any injury or illness in order of severity</p>
    <p class="call">CALL 000<br>FOR AMBULANCE, POLICE OR FIRE</p>
  </aside>

  <table class="triage-table">
    <colgroup>
      <col style="width:187px"><col style="width:202px"><col style="width:194px"><col style="width:216px">
      <col style="width:203px"><col style="width:192px"><col style="width:177px">
    </colgroup>
    <thead>
      <tr>
        <th class="instruction">Instruction</th>
        <th class="c1">Category 1</th><th class="c2">Category 2</th><th class="c3">Category 3</th>
        <th class="c4">Category 4</th><th class="c5">Category 5</th><th class="c6">Category 6</th>
      </tr>
    </thead>
    <tbody>
      <tr class="symptoms">
        <td>Practice to ask the patient or caller to describe the problem/s, and catego­rise accordingly:</td>
        <td>• Chest pain<br>• Breathing difficulties/ trouble talking<br>• Facial swelling and rash<br>• Collapse/altered consciousness<br>• Facial/limb weakness<br>• Extensive burns<br>• Sick patient you have concerns about</td>
        <td>• Fitting<br>• Bleeding (heavy or persistent)<br>• Spinal or head injury/ trauma<br>• Snake bite<br>• Heart palpitations<br>• In labour/ruptured membranes<br>• Neck stiffness/altered consciousness</td>
        <td>• Unable to urinate<br>• Unwell 'floppy' infant<br>• Poisoning/overdose<br>• Eye injuries/chemical in the eye<br>• Pain (severe)<br>• Injured limb/possible fracture</td>
        <td>• Unwell child/elder with fever, vomiting, diarrhoea or pain for &gt;24 hours<br>• Pregnancy: pain or bleed­ing; reduced foetal move­ment<br>• Abuse or assault<br>• Visual disturbance<br>• Patient or carer with extreme concern<br>• Psychological distress</td>
        <td>• Unwell child/elderly with fever, vomiting, diarrhoea or pain for &lt;24 hours<br>• Rash (severe)<br>• Cut/laceration<br>• Severe flu like symptoms</td>
        <td>• Adult with fever, but otherwise well<br>• Post op problems<br>• Eye or ear infections/pain<br>• Adult with continuous vomiting and/or diarrhoea for &gt;24 hrs</td>
      </tr>
      <tr class="action">
        <td>Tell the caller to:</td>
        <td><strong>Call 000</strong></td>
        <td><strong>Go to emergency depart­ment now</strong></td>
        <td><strong>Put call through to nurse/doctor</strong></td>
        <td><strong>Come to surgery now Advise the on-call nurse/doctor</strong></td>
        <td><strong>Come to surgery today and call back if gets worse</strong></td>
        <td><strong>Make an appointment within 24 hours and call back if gets worse</strong></td>
      </tr>
      <tr class="staff">
        <td>Practice/<br>Receptionist</td>
        <td><strong>Call nurse/doctor for help immediately</strong></td>
        <td><strong>Interrupt nurse/doctor immediately</strong></td>
        <td><strong>Advise nurse/doctor now</strong></td>
        <td><strong>Discuss with nurse/doctor</strong></td>
        <td><strong>Inform nurse/doctor within 30 minutes</strong></td>
        <td><strong>Inform nurse/doctor</strong></td>
      </tr>
      <tr class="admin">
        <td>Practice/<br>Receptionist</td>
        <td>Retrieve patient file<br>Document activity</td>
        <td>Retrieve patient file<br>Document activity</td>
        <td>Retrieve patient file<br>Document activity</td>
        <td>Retrieve patient file<br>Document activity</td>
        <td>Retrieve patient file<br>Document activity</td>
        <td>Retrieve patient file<br>Document activity</td>
      </tr>
    </tbody>
  </table>

  <div class="rule bottom"></div>
  <p class="credits">Harcourt College produced with permissions from Outback Care Alliance, produced by Outback Care Alliance with Clinic Circle Uptown with permissions from Southern Lakes Carewell Hub. Harcourt acknowledges the NBFPS Standards Criterion 3.2.3 Practice Training and Education in Triage</p>
</main>
</body>
</html>
```